Church Lanterns Over Millbrook Gospel Booklet Design

We need a booklet designed that we will be printing to hand out in our community. Wording for each page will be provided and we need graphic design to produce the layouts in a format ready for print. Booklet will be 4.75" x 4.75" square and a total of 12 pages: 1 cover page front, 1 cover page back, 10 inside pages some of which will be full spread across 2 pages.

Target Market(s)

English speaking Westerners

Industry/Entity Type

Religious

Font styles to use
Serif

Colors
ffffff
85abd2
0292cd
33b8a4
5c5c5c

Requirements
Must have
• Minimalist design with clean look described in attached document
Nice to have
• Aesthetically pleasing graphics, crisp fonts, excellent turn around times
Should not have
• Effeminate design, busy look with too much graphic and text

```html
<!DOCTYPE html>
<html lang="en">
<head>
<meta charset="utf-8">
<title>Lanterns Over Millbrook – Booklet Spread, Pages 10–11</title>
<link rel="stylesheet" href="https://fonts.googleapis.com/css2?family=Inter:ital,wght@0,400;1,400&family=Roboto+Condensed:ital,wght@0,400;1,600;1,700&display=swap">
<style>
  :root {
    --paper: #ffffff;
    --ink: #3a3a3a;
    --verse-ink: #ffffff;
    --sky-top: #b9cadc;
    --sky-mid: #8ea8c4;
    --ridge-mid: #4d6176;
    --ridge-deep: #27313c;
    --ridge-base: #161b21;
  }
  * { margin: 0; padding: 0; box-sizing: border-box; }
  html, body {
    width: 1200px;
    height: 600px;
    overflow: hidden;
    background: var(--paper);
  }
  .spread {
    position: relative;
    width: 1200px;
    height: 600px;
    display: flex;
  }
  .page {
    position: relative;
    width: 600px;
    height: 600px;
  }
  .page--text { background: var(--paper); }
  .body-copy {
    position: absolute;
    left: 62px;
    top: 207px;
    width: 470px;
    font-family: "Inter", Arial, sans-serif;
    font-size: 18.4px;
    line-height: 24.6px;
    color: var(--ink);
  }
  .folio {
    position: absolute;
    left: 60px;
    top: 532px;
    font-family: "Inter", Arial, sans-serif;
    font-style: italic;
    font-size: 16px;
    color: var(--ink);
  }
  .page--verse { overflow: hidden; }
  .landscape {
    position: absolute;
    inset: 0;
    background: linear-gradient(180deg,
      var(--sky-top) 0%,
      var(--sky-mid) 28%,
      var(--ridge-mid) 52%,
      var(--ridge-deep) 75%,
      var(--ridge-base) 100%);
  }
  .verse {
    position: absolute;
    inset: 0;
    text-align: center;
    color: var(--verse-ink);
    font-family: "Roboto Condensed", "Arial Narrow", sans-serif;
    text-transform: uppercase;
  }
  .verse__line {
    position: absolute;
    left: 0;
    right: 0;
    font-style: italic;
    font-weight: 600;
    letter-spacing: -0.6px;
  }
  .verse__line--lead { top: 183px; font-size: 17px; }
  .verse__line--confession { top: 225px; font-size: 29px; font-weight: 700; letter-spacing: -1px; }
  .verse__line--belief { top: 277px; font-size: 16px; line-height: 24px; }
  .verse__line--promise { top: 345px; font-size: 29px; font-weight: 700; letter-spacing: -1px; }
  .verse__reference {
    position: absolute;
    left: 0;
    right: 0;
    top: 520px;
    font-size: 15.5px;
    font-weight: 400;
    letter-spacing: 0.3px;
  }
</style>
</head>
<body>
  <main class="spread">
    <section class="page page--text">
      <p class="body-copy">Next, God has given us the Bible and his church as the key tools for us to grow in our understanding of God and our personal relationship with him. So, it is essential you find a local church that believes the Bible is 100% true. Tell one of the pastors you are a brand new Christian and they will help you from there.</p>
      <span class="folio">10</span>
    </section>
    <section class="page page--verse">
      <div class="landscape" role="img" aria-label="Photograph of layered misty blue mountain ridges under a pale sky, darkening towards forested hills at the bottom"></div>
      <blockquote class="verse">
        <p class="verse__line verse__line--lead">If you confess with your mouth.</p>
        <p class="verse__line verse__line--confession">“Jesus is Lord, ”</p>
        <p class="verse__line verse__line--belief">And believe in your heart that God raised him<br>from the dead,</p>
        <p class="verse__line verse__line--promise">You will be saved.</p>
        <cite class="verse__reference">Romans 10:9</cite>
      </blockquote>
    </section>
  </main>
</body>
</html>
```